Design an engaging, visually attractive and well laid out Word Press website

I have a partially completed Word Press website that I need to have completed . The previous designer overestimated her ability to produce a quality product and underestimated my knowledge of how a good well designed website should look visually and be laid out.

A visitor to the site should have a clear understanding of the services offered by the business, be able to navigate the site with ease via effective logical pathways, have calls to action that are prominent and located in the correct locations that prompt the viewer to make contact when they are ready to act. The site needs to be visually impactful, have lots of white space, fast loading and mobile compatible and the visitor needs to have the impression that they need to look no further for the services offered.

I am particularly interested in how you think the Services and Projects pages should be best laid out so they present well on a mobile device without looking cluttered and can be navigated and viewed with ease.

I have the copy and images (these may need some changes) and I have put together a basic version of a layout on MS Word documents. These are all in a Dropbox folder (link below). I am open to a designer offering his/her own thoughts on how the site can be laid out better. Also I have a link below to the partially created website. I will need the website coded once I am happy with the design.

Links:

https://fernlotyards.com.au?bypass=farm

https://www.filecrate.example/sh/qrwpx8m3vd452kt/BBBDmwkqwwCqUbmKjAZ7OH-7b?dl=0

Target Market(s)

Primarily females aged 19 - 65 who work for a strata management and/or a property management company. These organisations oversee the maintenance aspects for apartments/condominiums and manage the properties on behalf of the owners.
The business that the website represents provides professional gardening services for commercial businesses and these apartment/condominium communities. So do not think home gardens and that type of gardening. Think on a larger scale like commercial businesses, hospitals, blocks of units/apartments/condominiums, shopping centres.

Industry/Entity Type

Commercial

Coding

Coded - Design and coding required

Number of Pages Required

5+ page

Requirements
Must have
• A great layout with lots of white space, intuitive navigation, prominent calls to action and professional looking.

The website needs to give the impression that the business is mid-size with a number of employees i.e. 6-10, yet still have the impression that it is a business where the owner is involved and there is a high level of personalised customer service.
Nice to have
• Maybe a looping video on the home page that is faded in the background that represents what the business does and who it services.
Should not have
• An attitude by the designer that anything will satisfy me. I want the designer to create a design that they would be proud to present to the market.

I have had too many bad experiences with website designers who do not have the appropriate attitude or skills to produce a quality site that appeals to me.

```html
<!DOCTYPE html>
<html lang="en">
<head>
<meta charset="utf-8">
<title>Garden Care | Fernlot Yards</title>
<link href="https://fonts.googleapis.com/css2?family=Oswald:wght@400;500&family=Lato:wght@400;700&display=swap" rel="stylesheet">
<style>
:root{
  --green:#7fbd42;
  --green-dark:#6aa532;
  --slate:#6f7b7b;
  --charcoal:#383838;
  --ink:#222;
  --text:#555;
  --muted:#999;
  --panel:#f3f3f3;
  --line:#e2e2e2;
  --footer:#0b0b0b;
  --bottom:#000;
}
*{box-sizing:border-box;margin:0;padding:0}
html,body{width:1200px;height:2315px;overflow:hidden}
body{font-family:'Lato',sans-serif;color:var(--text);background:#fff;position:relative}
.wrap{width:878px;margin-left:161px;position:relative}
a{color:inherit;text-decoration:none}

/* top bar */
.topbar{height:41px;background:var(--slate);color:#fff;font-size:11px}
.topbar .wrap{display:flex;align-items:center;height:41px}
.topbar .item{display:flex;align-items:center;gap:7px}
.topbar .sep{margin:0 12px;opacity:.6}
.topbar .socials{margin-left:auto;display:flex;gap:8px}
.soc-sq{width:20px;height:20px;background:#8a9595;border-radius:2px}

/* header */
.header{height:86px;background:var(--charcoal)}
.header .wrap{display:flex;align-items:center;height:86px}
.brand{display:flex;align-items:center;gap:9px}
.brand-mark{width:26px;height:26px;background:var(--green)}
.brand-name{font-family:'Lato',sans-serif;font-weight:700;font-size:18px;color:var(--green);letter-spacing:1px}
.nav{display:flex;gap:29px;margin-left:153px;font-family:'Oswald',sans-serif;font-size:13.5px;color:#fff;text-transform:uppercase}
.btn{display:inline-flex;align-items:center;justify-content:center;background:var(--green);color:#fff;font-family:'Oswald',sans-serif;font-weight:500;font-size:11.5px;width:98px;height:38px;text-transform:uppercase}
.header .btn{margin-left:auto}

/* page title */
.page-title{height:171px;background:#f4f4f4;position:relative;border-bottom:1px solid #eee;overflow:hidden}
.page-title .photo{position:absolute;right:0;top:0;width:420px;height:100%;background:linear-gradient(90deg,rgba(244,244,244,1) 0%,rgba(190,205,170,.7) 45%,#9fb083 75%,#7e9466 100%)}
.page-title h1{position:absolute;left:167px;top:68px;font-family:'Oswald',sans-serif;font-weight:500;font-size:29px;color:var(--slate);letter-spacing:.3px}
.crumbs{position:absolute;right:161px;top:78px;font-family:'Oswald',sans-serif;font-size:12px;color:#999;display:flex;gap:8px;z-index:1}
.crumbs .current{color:var(--green)}

/* intro */
.intro{padding-top:76px;height:545px}
.intro .wrap{display:flex;justify-content:space-between}
.intro-copy{width:430px}
.intro h2{font-family:'Oswald',sans-serif;font-weight:500;font-size:28px;color:var(--ink);margin-top:4px}
.intro p{font-size:12px;line-height:22.5px;margin-top:20px;padding-left:2px}
.intro-photo{width:412px;height:178px;border:2px solid #e4e4e4;background:linear-gradient(120deg,#6a9a24,#4f8a1e 45%,#8fae4e 70%,#b09a7a 85%,#9c8460)}

/* accordion */
.accordion{width:878px;margin-left:161px;position:absolute;top:607px}
.acc-item{height:60px;background:var(--panel);border-bottom:1px solid var(--line);display:flex;align-items:center;padding:0 29px;font-family:'Oswald',sans-serif;font-size:17px;color:#333;text-transform:uppercase}
.acc-item .toggle{margin-left:auto;width:14px;height:14px;position:relative}
.acc-item .toggle::before,.acc-item .toggle::after{content:"";position:absolute;background:#333}
.acc-item .toggle::before{left:0;top:6px;width:14px;height:2px}
.acc-item .toggle::after{left:6px;top:0;width:2px;height:14px}
.acc-item.open{background:var(--green);color:#fff;border-bottom:none}
.acc-item.open .toggle::before{background:#fff}
.acc-item.open .toggle::after{display:none}
.acc-body{height:430px;border:1px solid var(--line);border-top:none;padding:33px 29px 0;background:#fff}
.acc-body p{font-size:12px;line-height:22.5px}
.gallery{display:flex;justify-content:space-between;margin:20px 0 18px}
.gallery .shot{width:153px;height:123px;border:1px solid #ddd;padding:2px}
.gallery .shot span{display:block;width:100%;height:100%}
.extras{border-top:1px solid var(--line);margin-top:22px;height:90px;display:flex;align-items:center}
.extras h4{font-weight:400;font-size:15.5px;color:var(--ink);width:360px}
.extra{display:flex;align-items:center;gap:12px;font-size:12px;line-height:16px;color:#444;padding:0 37px;border-left:1px solid #ddd;height:30px}
.extra:first-of-type{border-left:none;padding-left:0}
.extra:last-child{padding-right:0}

/* pager */
.pager{position:absolute;top:1609px;left:161px;width:878px;display:flex;justify-content:space-between;font-family:'Oswald',sans-serif;font-size:11.5px;text-transform:uppercase}
.pager a{display:flex;align-items:center;gap:8px}
.pager .prev{color:var(--muted)}
.pager .next{color:var(--green)}

/* cta */
.cta{position:absolute;top:1697px;left:0;width:1200px;height:221px;border-top:1px solid #eee}
.cta h3{position:absolute;left:160px;top:80px;font-family:'Oswald',sans-serif;font-weight:500;font-size:24px;color:var(--green)}
.cta p{position:absolute;left:160px;top:119px;font-size:12px;color:#444}
.cta p u{color:#444}
.cta .figure{position:absolute;left:625px;top:34px;width:200px;height:187px;background:linear-gradient(180deg,#3d8a3a 0%,#2f6b2f 60%,#3a5a35 100%);border-radius:60px 60px 0 0}
.cta .btn{position:absolute;left:941px;top:90px}

/* footer */
.footer{position:absolute;top:1918px;left:0;width:1200px;height:332px;background:var(--footer);color:#fff}
.footer .brand{position:absolute;left:160px;top:77px}
.footer .about{position:absolute;left:160px;top:148px;width:210px;font-size:12px;line-height:22.5px}
.footer h5{font-family:'Oswald',sans-serif;font-weight:500;font-size:23px}
.footer h5::after{content:"";display:block;width:30px;height:2px;background:var(--green);margin-top:10px}
.quick{position:absolute;left:550px;top:68px}
.quick ul{list-style:none;margin-top:17px;font-size:12px}
.quick li{height:28.5px}
.contact{position:absolute;left:835px;top:68px;width:204px}
.contact .row{display:flex;align-items:center;gap:12px;font-size:12px;height:28.5px}
.contact .row:first-of-type{margin-top:17px}
.contact .find{border-top:1px solid #2b2b2b;margin-top:14px;padding-top:15px;display:flex;align-items:center;font-size:12px}
.contact .find .sq{width:30px;height:30px;border-radius:2px;background:#6f7b7b;margin-left:8px}
.contact .find .sq.on{background:var(--green)}
.contact .find span{margin-right:8px}

.bottombar{position:absolute;top:2250px;left:0;width:1200px;height:65px;background:var(--bottom);color:#fff;font-size:11.5px}
.bottombar .copy{position:absolute;left:160px;top:25px}
.bottombar .legal{position:absolute;right:161px;top:26px;display:flex;gap:10px}
</style>
</head>
<body>

<div class="topbar">
  <div class="wrap">
    <span class="item">
      <svg width="11" height="11" viewBox="0 0 24 24"><path fill="#fff" d="M6.6 10.8a15.1 15.1 0 0 0 6.6 6.6l2.2-2.2c.3-.3.7-.4 1-.2 1.1.4 2.3.6 3.6.6.6 0 1 .4 1 1V20c0 .6-.4 1-1 1C10.6 21 3 13.4 3 4c0-.6.4-1 1-1h3.5c.6 0 1 .4 1 1 0 1.3.2 2.5.6 3.6.1.3 0 .7-.2 1z"/></svg>
      0400 555 182
    </span>
    <span class="sep">|</span>
    <span class="item">
      <svg width="11" height="9" viewBox="0 0 24 18"><path fill="#fff" d="M0 0h24v18H0z"/><path fill="#6f7b7b" d="M2 2l10 7 10-7v1.5L12 11 2 3.5z"/></svg>
      owen@fernlotyards.com.au
    </span>
    <div class="socials"><span class="soc-sq"></span><span class="soc-sq"></span><span class="soc-sq"></span></div>
  </div>
</div>

<header class="header">
  <div class="wrap">
    <a class="brand" href="#"><span class="brand-mark"></span><span class="brand-name">FERNLOT YARDS</span></a>
    <nav class="nav"><a>Home</a><a>About</a><a>Services</a><a>Work</a><a>Contact</a></nav>
    <a class="btn" href="#">Free Quote</a>
  </div>
</header>

<section class="page-title">
  <div class="photo" role="img" aria-label="Gardener trimming hedges in a green garden"></div>
  <h1>GARDEN CARE</h1>
  <div class="crumbs"><span>Home</span><span>»</span><span>Services</span><span>»</span><span class="current">Garden Care</span></div>
</section>

<section class="intro">
  <div class="wrap">
    <div class="intro-copy">
      <h2>Garden Care &amp; Programs</h2>
      <p>Our garden care service offers individually tailored programs so you garden looks great all year round. Regular visits are scheduled depending upon the needs and budgets of the individual clients. Our programs incorporate regular fertilizing, weed control and reticulation audits. View below all we have to offer in our garden care programs.</p>
    </div>
    <div class="intro-photo" role="img" aria-label="Aerial view of a gardener mowing a lawn beside a gravel path"></div>
  </div>
</section>

<div class="accordion">
  <div class="acc-item">Lawn Care<span class="toggle"></span></div>
  <div class="acc-item">Pruning &amp; Hedging<span class="toggle"></span></div>
  <div class="acc-item open">Weed Control<span class="toggle"></span></div>
  <div class="acc-body">
    <p>We provide weed control solutions for gardens, lawns and paved areas. We use a post emergent herbicide and we can combine that with a pre-emergent herbicide. We also provide non-chemical solutions.</p>
    <div class="gallery">
      <div class="shot"><span role="img" aria-label="Gloved hand pulling weeds from soil" style="background:linear-gradient(135deg,#4d6b2a,#7a9a3c,#3a4a22)"></span></div>
      <div class="shot"><span role="img" aria-label="Wheelbarrow full of garden waste on a lawn" style="background:linear-gradient(135deg,#8aa04a,#5f7d30,#9aa070)"></span></div>
      <div class="shot"><span role="img" aria-label="Gardener hoeing weeds in a garden bed" style="background:linear-gradient(135deg,#6d8a3a,#4a3a2a,#7a6048)"></span></div>
      <div class="shot"><span role="img" aria-label="Line trimmer cutting weeds among yellow flowers" style="background:linear-gradient(135deg,#6fa03a,#4f8a28,#8ab84a)"></span></div>
      <div class="shot"><span role="img" aria-label="Hand spraying herbicide on weeds" style="background:linear-gradient(135deg,#a9cf5a,#7fb23c,#e8ecd8)"></span></div>
    </div>
    <p>When a pre-emergent herbicide is applied to turf or gardens, the number of annual weeds is effectively reduced, thereby limiting the need to re-apply after the initial treatment. This also reduces the weed’s seed bank that could potentially germinate in future years. Weed control is an essential aspect of having a well-presented garden, lawns, pathways and driveways.</p>
    <div class="extras">
      <h4>The additional services we offer to control weeds:</h4>
      <div class="extra">
        <svg width="34" height="30" viewBox="0 0 34 30" fill="none" stroke="#7fbd42" stroke-width="1.4"><path d="M10 29V15M10 18c-4 0-7-3-7-6 4 0 7 2 7 6zM10 16c0-4 3-7 7-7 0 4-3 7-7 7zM3 29h14"/><path d="M26 16V6M26 6c-3 0-4-3-4-5 3 0 4 2 4 5zM26 6c0-3 2-5 5-5 0 3-2 5-5 5z"/><path d="M22 16h8l-1 6h-6z"/></svg>
        <span>Planting ground<br>cover plants</span>
      </div>
      <div class="extra">
        <svg width="34" height="30" viewBox="0 0 34 30" fill="none" stroke="#7fbd42" stroke-width="1.4"><path d="M10 29V15M10 18c-4 0-7-3-7-6 4 0 7 2 7 6zM10 16c0-4 3-7 7-7 0 4-3 7-7 7zM3 29h14"/><path d="M26 16V6M26 6c-3 0-4-3-4-5 3 0 4 2 4 5zM26 6c0-3 2-5 5-5 0 3-2 5-5 5z"/><path d="M22 16h8l-1 6h-6z"/></svg>
        <span>Solarisation</span>
      </div>
      <div class="extra">
        <svg width="34" height="30" viewBox="0 0 34 30" fill="none" stroke="#7fbd42" stroke-width="1.4"><path d="M10 29V15M10 18c-4 0-7-3-7-6 4 0 7 2 7 6zM10 16c0-4 3-7 7-7 0 4-3 7-7 7zM3 29h14"/><path d="M26 16V6M26 6c-3 0-4-3-4-5 3 0 4 2 4 5zM26 6c0-3 2-5 5-5 0 3-2 5-5 5z"/><path d="M22 16h8l-1 6h-6z"/></svg>
        <span>Mulching</span>
      </div>
    </div>
  </div>
  <div class="acc-item">Couch Grass Edition<span class="toggle"></span></div>
  <div class="acc-item">Soil Improvement<span class="toggle"></span></div>
  <div class="acc-item">Fertilizing<span class="toggle"></span></div>
  <div class="acc-item">Mulching<span class="toggle"></span></div>
  <div class="acc-item">Pests &amp; Disease<span class="toggle"></span></div>
  <div class="acc-item" style="border-bottom:none">Rubbish Removal<span class="toggle"></span></div>
</div>

<nav class="pager">
  <a class="prev" href="#"><svg width="14" height="8" viewBox="0 0 14 8" fill="none" stroke="#999" stroke-width="1"><path d="M14 4H1M4 1L1 4l3 3"/></svg>Previous Service</a>
  <a class="next" href="#">Next Service<svg width="14" height="8" viewBox="0 0 14 8" fill="none" stroke="#7fbd42" stroke-width="1"><path d="M0 4h13M10 1l3 3-3 3"/></svg></a>
</nav>

<section class="cta">
  <h3>Is your garden overgrown with weeds?</h3>
  <p>Request a free quote now or call us at <u>0400 555 182</u></p>
  <div class="figure" role="img" aria-label="Smiling gardener in green cap and apron holding hedge shears and secateurs"></div>
  <a class="btn" href="#">Free Quote</a>
</section>

<footer class="footer">
  <a class="brand" href="#"><span class="brand-mark"></span><span class="brand-name">FERNLOT YARDS</span></a>
  <p class="about">Scheduled Garden Care Programs and Garden Maintenance Services for residential, strata and commercial properties in Perth, WA</p>
  <div class="quick">
    <h5>Quick Links</h5>
    <ul><li>Home</li><li>About</li><li>Services</li><li>Work</li><li>Contact</li></ul>
  </div>
  <div class="contact">
    <h5>Contact</h5>
    <div class="row">
      <svg width="12" height="12" viewBox="0 0 24 24"><path fill="#7fbd42" d="M6.6 10.8a15.1 15.1 0 0 0 6.6 6.6l2.2-2.2c.3-.3.7-.4 1-.2 1.1.4 2.3.6 3.6.6.6 0 1 .4 1 1V20c0 .6-.4 1-1 1C10.6 21 3 13.4 3 4c0-.6.4-1 1-1h3.5c.6 0 1 .4 1 1 0 1.3.2 2.5.6 3.6.1.3 0 .7-.2 1z"/></svg>
      0400 555 182
    </div>
    <div class="row">
      <svg width="12" height="9" viewBox="0 0 24 18"><path fill="#7fbd42" d="M0 0h24v18H0z"/><path fill="#0b0b0b" d="M2 2l10 7 10-7v1.5L12 11 2 3.5z"/></svg>
      owen@fernlotyards.com.au
    </div>
    <div class="find"><span>Find Us Also At:</span><i class="sq"></i><i class="sq on"></i><i class="sq"></i></div>
  </div>
</footer>

<div class="bottombar">
  <span class="copy">© FERNLOT YARDS All Rights Reserved 2020</span>
  <span class="legal"><a>PRIVACY POLICY</a><span>|</span><a>TERMS OF USE</a></span>
</div>

</body>
</html>
```